Consulting Company Business Card

I am looking for a minimalist, classy, professional design on my business card. I would like it to be double-sided. I want to use the font and color scheme of my logo which are attached. Please be creative in the designs that you send me. I want to play off the design of my logo with the inner C that is Green and Blue broken up with the white.
Target Market(s)
Small Businesses
Industry/Entity Type
Consulting
Contact Information for Business Card
Derek L. Whitmore, CPA CGMA, 555-014-2283, dwhitmore@brovantadvisory.example, www.brovantadvisory.example

```html
<!DOCTYPE html>
<html lang="en">
<head>
<meta charset="utf-8">
<title>Brovant Advisory — Business Card</title>
<link href="https://fonts.googleapis.com/css2?family=Montserrat:wght@700;800&family=Open+Sans:wght@400&display=swap" rel="stylesheet">
<style>
  :root {
    --backdrop: #dcdcda;
    --card-white: #ffffff;
    --navy: #252b5c;
    --navy-deep: #1f254f;
    --navy-light: #3d4688;
    --teal: #2a8a86;
    --text-grey: #6a6a70;
    --rule: #3a3f63;
  }
  * { box-sizing: border-box; margin: 0; padding: 0; }
  html, body {
    width: 1200px; height: 801px; overflow: hidden;
    background: var(--backdrop);
  }
  .stage {
    position: relative; width: 1200px; height: 801px;
    display: flex; align-items: center; justify-content: center; gap: 40px;
  }
  .card {
    position: relative; width: 520px; height: 297px;
    box-shadow: 0 6px 18px rgba(0,0,0,0.18);
  }
  /* Front */
  .card-front { background: var(--card-white); }
  .brand-block {
    position: absolute; left: 30px; top: 0; width: 200px; height: 100%;
    display: flex; flex-direction: column; align-items: center; justify-content: center; gap: 10px;
  }
  .brand-mark {
    width: 26px; height: 26px; border-radius: 50%; background: var(--navy);
  }
  .brand-name {
    font-family: "Montserrat", sans-serif; font-weight: 800;
    color: var(--navy); font-size: 22px; letter-spacing: 1.5px;
    text-transform: uppercase; text-align: center; line-height: 1.15;
  }
  .divider {
    position: absolute; left: 250px; top: 98px; width: 1px; height: 104px;
    background: var(--rule);
  }
  .details {
    position: absolute; left: 272px; top: 92px;
  }
  .person-name {
    font-family: "Montserrat", sans-serif; font-weight: 800;
    color: var(--navy); font-size: 19px; letter-spacing: 0.5px; text-transform: uppercase;
  }
  .credentials {
    font-family: "Open Sans", sans-serif; color: var(--text-grey);
    font-size: 12px; margin-top: 2px; margin-bottom: 16px;
  }
  .contact-list { list-style: none; }
  .contact-list li {
    display: flex; align-items: center; gap: 7px;
    font-family: "Open Sans", sans-serif; color: var(--text-grey);
    font-size: 12px; line-height: 20px;
  }
  .contact-list svg { width: 11px; height: 11px; flex: none; fill: var(--teal); }
  /* Back */
  .card-back { background: var(--navy); overflow: hidden; }
  .back-pattern {
    position: absolute; inset: 0;
    background: linear-gradient(135deg, var(--navy-deep) 0%, var(--navy) 55%, var(--navy-light) 100%);
  }
  .back-brand {
    position: absolute; right: 40px; top: 50%; transform: translateY(-50%);
    display: flex; align-items: center; gap: 8px;
  }
  .back-brand .brand-mark { background: var(--card-white); width: 20px; height: 20px; }
  .back-brand .brand-name { color: var(--card-white); font-size: 15px; }
</style>
</head>
<body>
<main class="stage">
  <section class="card card-front" aria-label="Business card front">
    <div class="brand-block">
      <span class="brand-mark"></span>
      <span class="brand-name">Brovant<br>Advisory</span>
    </div>
    <div class="divider"></div>
    <div class="details">
      <h1 class="person-name">Derek L. Whitmore</h1>
      <p class="credentials">CPA CGMA</p>
      <ul class="contact-list">
        <li><svg viewBox="0 0 24 24"><path d="M6.6 10.8a15.1 15.1 0 0 0 6.6 6.6l2.2-2.2a1 1 0 0 1 1-.25 11.4 11.4 0 0 0 3.6.57 1 1 0 0 1 1 1V20a1 1 0 0 1-1 1A17 17 0 0 1 3 4a1 1 0 0 1 1-1h3.5a1 1 0 0 1 1 1c0 1.25.2 2.45.57 3.6a1 1 0 0 1-.25 1z"/></svg>555-014-2283</li>
        <li><svg viewBox="0 0 24 24"><path d="M2 5h20v14H2z M2 5l10 8 10-8" /></svg>dwhitmore@brovantadvisory.example</li>
        <li><svg viewBox="0 0 24 24"><circle cx="12" cy="12" r="10"/></svg>www.brovantadvisory.example</li>
      </ul>
    </div>
  </section>

  <section class="card card-back" aria-label="Business card back">
    <div class="back-pattern" role="img" aria-label="Embossed repeating monogram pattern in navy tones"></div>
    <div class="back-brand">
      <span class="brand-mark"></span>
      <span class="brand-name">Brovant Advisory</span>
    </div>
  </section>
</main>
</body>
</html>
```